Webdesign für ein Dachdeckerbetrieb
Zielgruppe
Wir sind ein Dachdeckerbetrieb.
Zielgruppe sind öffentliche Auftrageber , Hausverwaltungen und private Hausbesitzer.
Aufgabenstellung
Die Seite sollte übersichtlich sein. Nicht zuviele Menüs durch die man klicken muss.
Bilder können wir liefern .
Nach Vorgabe des Designers beschaffen wir die Bilder .
Logo ist vorhanden.

```html
<!DOCTYPE html>
<html lang="de">
<head>
<meta charset="utf-8">
<title>Kessler Dachbau – Über uns</title>
<link href="https://fonts.googleapis.com/css2?family=Roboto:wght@300;400;500;700&display=swap" rel="stylesheet">
<style>
:root{
  --green:#8cb021;
  --green-footer:#8fb022;
  --ink:#333537;
  --text:#6b6b6b;
  --hero:#4a4b4d;
  --band:#34373a;
  --grey:#f1f1f1;
  --white:#ffffff;
}
*{margin:0;padding:0;box-sizing:border-box}
html,body{width:736px;height:1200px;overflow:hidden}
body{position:relative;font-family:'Roboto',sans-serif;background:var(--white);color:var(--ink)}
.abs{position:absolute}
/* header */
.header{left:0;top:0;width:736px;height:44px;background:var(--white)}
.brand{left:144px;top:15px;font-size:12px;font-weight:700;color:var(--green);letter-spacing:.3px;display:flex;align-items:center;gap:4px}
.brand-dot{width:7px;height:7px;background:var(--green)}
.nav{left:280px;top:17px;display:flex;gap:16px;font-size:6.6px;color:var(--ink)}
.nav .active{color:var(--green);font-weight:500}
/* hero */
.hero{left:0;top:44px;width:736px;height:128px;background:linear-gradient(160deg,#555658,#404143 60%,#4b4c4e);text-align:center;color:var(--white)}
.hero h1{position:absolute;top:46px;width:100%;font-size:19px;font-weight:500;letter-spacing:-.3px}
.hero p{position:absolute;top:73px;width:100%;font-size:7.4px}
.hl{color:var(--green)}
/* badges & headings */
.badge{background:var(--green);color:var(--white);font-size:7.2px;padding:0 7px;height:15px;line-height:15px}
.heading{font-size:18.5px;font-weight:700;line-height:23px;letter-spacing:-.4px;color:var(--ink)}
.copy{font-size:6.4px;line-height:12.2px;color:var(--text);font-weight:300}
.copy b{font-weight:500;color:#555}
/* intro */
.intro-photo{left:144px;top:213px;width:218px;height:181px;border-radius:3px;background:linear-gradient(135deg,#c9cdd2 0%,#b9946e 30%,#d9774c 55%,#6a6a6c 100%)}
/* team */
.team-bg{left:0;top:450px;width:736px;height:536px;background:var(--grey)}
.member{width:104px}
.member .photo{width:104px;height:107px;border-radius:3px}
.member h3{margin-top:12px;font-size:8.3px;font-weight:500;color:var(--ink);letter-spacing:-.1px}
.member p{margin-top:2px;font-size:6px;color:var(--text)}
.btn{left:329px;top:929px;width:77px;height:23px;background:var(--green);color:var(--white);font-size:6px;font-weight:500;text-align:center;line-height:23px;border-radius:2px}
/* call band */
.band{left:0;top:986px;width:736px;height:48px;background:var(--band)}
.band-line{left:0;top:984px;width:736px;height:2px;background:#c9c9c9}
.ask{left:155px;top:1004px;font-size:10.6px;color:var(--white);font-weight:500}
.ask span{color:var(--green);font-weight:300}
.phone-icon{left:420px;top:1002px}
.hotline{left:444px;top:1005px;font-size:9px;font-weight:700;color:var(--white)}
/* footer */
.footer{left:0;top:1034px;width:736px;height:166px;background:var(--green-footer);color:var(--white)}
.fcol h4{font-size:7.3px;font-weight:500;margin-bottom:8px}
.fcol ul{list-style:none;font-size:6.3px}
.fcol li{height:17.3px}
.fcol li::before{content:"»";margin-right:5px}
.callback p{font-size:6px;line-height:11.7px;width:92px}
.field{width:94px;height:15px;background:var(--white);font-size:5px;color:#999;padding-left:6px;line-height:15px;margin-top:3px}
.send{width:49px;height:17px;border:1px solid var(--white);border-radius:2px;font-size:6px;font-weight:700;text-align:center;line-height:15px;margin-top:5px}
.fbrand{left:481px;top:1073px;font-size:10px;font-weight:700;display:flex;align-items:center;gap:4px}
.fbrand .dot{width:6px;height:6px;background:var(--white)}
.contact{left:481px;top:1106px;font-size:6.2px}
.contact div{display:flex;align-items:center;gap:6px;height:12px}
.socials{left:478px;top:1153px;display:flex;gap:3px}
.socials span{width:14px;height:14px;border:1px solid var(--white);border-radius:50%}
</style>
</head>
<body>

<header class="abs header">
  <div class="abs brand"><span class="brand-dot"></span>KESSLER DACHBAU</div>
  <nav class="abs nav">
    <span>Startseite</span><span class="active">Über uns</span><span>Referenzen</span><span>Leistungen</span><span>Kontakt</span>
  </nav>
</header>

<section class="abs hero">
  <h1>Über uns</h1>
  <p><span class="hl">SIE</span> stehen bei uns <span class="hl">im Mittelpunkt</span></p>
</section>

<div class="abs intro-photo" role="img" aria-label="Dachdecker verlegt rote Dachziegel auf Holzlatten"></div>
<div class="abs badge" style="left:407px;top:213px">Wir sind ihr Partner</div>
<h2 class="abs heading" style="left:406px;top:234px;width:190px">Für ausdrucksstarke Dächer</h2>
<div class="abs copy" style="left:407px;top:286px;width:180px">
  <p>Unser Fachbetrieb ist Ihr zuverlässiger und fachkundiger Partner in allen Fragen rund um das Thema Bedachungen. Wir unterstützen Sie bei der Planung und Durchführung von sämtlichen Dachdeckerarbeiten.</p>
  <p style="margin-top:12.2px">Bei unserer Arbeit überzeugen vor allem durch fachliche Kompetenz und viel Erfahrung. Wir arbeiten mit Ihnen zusammen – auch in schwindelerregender Höhe.<br><b>Sie stellen uns Aufgaben und wir lösen diese individuell</b></p>
</div>

<div class="abs team-bg"></div>
<div class="abs badge" style="left:145px;top:487px">Ihre Aufgaben</div>
<h2 class="abs heading" style="left:144px;top:509px">Lösen wir individuell</h2>
<p class="abs copy" style="left:145px;top:539px;width:440px">Sie suchen starke und zuverlässige Dachdecker oder Zimmerer für Ihre Dachsanierung?<br>Unsere Dachdecker und Zimmerer bauen Ihnen ein qualitativ hochwertiges Dach, das Sie bei „Wind und Wetter“ schützt und Ihnen ein sicheres und langlebiges Zuhause bietet.</p>

<div class="abs member" style="left:144px;top:599px"><div class="photo" role="img" aria-label="Porträtfoto Geschäftsführer" style="background:linear-gradient(160deg,#2f4a25,#5b7a3c 50%,#b8c0cc)"></div><h3>Jonas Brenning</h3><p>Geschäftsführer</p></div>
<div class="abs member" style="left:259px;top:599px"><div class="photo" role="img" aria-label="Porträtfoto Buchhaltung" style="background:linear-gradient(160deg,#e9dfd0,#c9a57e 50%,#3a3432)"></div><h3>Petra Brenning</h3><p>Buchhaltung</p></div>
<div class="abs member" style="left:374px;top:599px"><div class="photo" role="img" aria-label="Porträtfoto Schreinermeister" style="background:linear-gradient(160deg,#2b3033,#55504a 50%,#23272a)"></div><h3>Lukas Brenning</h3><p>Schreinermeister</p></div>
<div class="abs member" style="left:489px;top:599px"><div class="photo" role="img" aria-label="Porträtfoto Dachdecker" style="background:linear-gradient(160deg,#8b8d8f,#4d4846 50%,#1f1f21)"></div><h3>Felix Brenning</h3><p>Dachdecker</p></div>

<div class="abs member" style="left:144px;top:757px"><div class="photo" role="img" aria-label="Porträtfoto Sachbearbeiterin" style="background:linear-gradient(160deg,#efefef,#d8c8bb 50%,#f4f4f4)"></div><h3>Karin Vogt</h3><p>Sachbearbeiterin</p></div>
<div class="abs member" style="left:258px;top:757px"><div class="photo" role="img" aria-label="Porträtfoto Schreinermeister" style="background:linear-gradient(160deg,#b7aea3,#9a8a7e 50%,#2f3438)"></div><h3>Dieter Haller</h3><p>Schreinermeister</p></div>
<div class="abs member" style="left:373px;top:757px"><div class="photo" role="img" aria-label="Porträtfoto Auszubildender Dachdecker" style="background:linear-gradient(160deg,#e6e6e6,#cfb39a 50%,#d9dcdb)"></div><h3>Nico Fuchs</h3><p>Azubi zum Dachdecker</p></div>
<div class="abs member" style="left:488px;top:757px"><div class="photo" role="img" aria-label="Porträtfoto Dachdecker" style="background:linear-gradient(160deg,#c9a83a,#8a6a4c 50%,#6c7f96)"></div><h3>Stefan Reuter</h3><p>Dachdecker</p></div>

<div class="abs btn">Kontakt aufnehmen</div>

<div class="abs band-line"></div>
<section class="abs band"></section>
<p class="abs ask">Haben Sie weitere Fragen? <span>Wir haben die Antworten!</span></p>
<svg class="abs phone-icon" width="18" height="18" viewBox="0 0 24 24" fill="none" stroke="#8cb021" stroke-width="1.5" stroke-linecap="round" stroke-linejoin="round"><path d="M22 16.9v3a2 2 0 0 1-2.2 2 19.8 19.8 0 0 1-8.6-3.1 19.5 19.5 0 0 1-6-6A19.8 19.8 0 0 1 2.1 4.2 2 2 0 0 1 4.1 2h3a2 2 0 0 1 2 1.7c.1.9.4 1.8.7 2.7a2 2 0 0 1-.5 2.1L8 9.8a16 16 0 0 0 6 6l1.3-1.3a2 2 0 0 1 2.1-.4c.9.3 1.8.6 2.7.7a2 2 0 0 1 1.7 2z"/></svg>
<p class="abs hotline">von 8-17 Uhr: 0 61 20 - 45 67 80</p>

<footer class="abs footer"></footer>
<div class="abs fcol" style="left:155px;top:1069px;color:#fff"><h4>Navigation</h4><ul><li>Startseite</li><li>Über uns</li><li>Referenzen</li><li>Leistungen</li><li>Kontakt</li></ul></div>
<div class="abs fcol" style="left:247px;top:1069px;color:#fff"><h4>Rechtliches</h4><ul><li>Datenschutz</li><li>AGB</li><li>Impressum</li></ul></div>
<div class="abs fcol callback" style="left:344px;top:1069px;color:#fff">
  <h4>Rückrufservice</h4>
  <p>Wir rufen Sie schnellst möglich an und helfen Ihnen weiter!</p>
  <div class="field">Ihr Name</div>
  <div class="field">Telefonnummer</div>
  <div class="send">absenden</div>
</div>
<div class="abs fbrand" style="color:#fff"><span class="dot"></span>KESSLER DACHBAU</div>
<div class="abs contact" style="color:#fff">
  <div><svg width="7" height="7" viewBox="0 0 24 24" fill="none" stroke="#fff" stroke-width="2"><path d="M12 22s7-6.5 7-12a7 7 0 0 0-14 0c0 5.5 7 12 7 12z"/><circle cx="12" cy="10" r="2.5"/></svg>Lindenweg 12, 55299 Musterau</div>
  <div><svg width="7" height="7" viewBox="0 0 24 24" fill="none" stroke="#fff" stroke-width="2"><rect x="3" y="5" width="18" height="14" rx="1"/><path d="M3 6l9 7 9-7"/></svg>info@kessler-dachbau.example</div>
  <div><svg width="7" height="7" viewBox="0 0 24 24" fill="none" stroke="#fff" stroke-width="2"><path d="M22 16.9v3a2 2 0 0 1-2.2 2A19.8 19.8 0 0 1 2.1 4.2 2 2 0 0 1 4.1 2h3a2 2 0 0 1 2 1.7l.7 2.7-1.8 3.4a16 16 0 0 0 6 6l3.4-1.8 2.7.7a2 2 0 0 1 1.7 2z"/></svg>06120 - 45 67 80</div>
</div>
<div class="abs socials"><span></span><span></span><span></span></div>

</body>
</html>
```